"Inkvale" printing shop

-The design must be based around the attached HPID (home page information design) called "Inkvale - HPID".

The table boxes are just for approximate placement of information – you DON'T have to box everything in and you can arrange these. All fonts used in the HPID are only examples - you can use any Google font you wish.

- Information only is in orange text. Copy to go on the design in black text. Some instructions are in the HPID. Please be creative!

-The design needs to be modern. Colours are to be consistent with their new logo or complement it. Keep it clean and simple, you don't need to use lots of colours. Use lots of white.

- images / icons for the site need to be relevant and high quality, but they must also be free images or icons. I have attached a few examples that could be used.

Width of content will be 1100 pixels when implemented as a web page. Header height (without nav bar) 150-200 pixels.

If your design is chosen the winning PSD file will have to be provided as follows…
1. Canvas size of 2000px x 2000px - 72ppi in Adobe Photoshop (CS5 compatible)
2. Width of content section is 1100px wide - centered in the canvas
3. Any button rollovers/hovers in the PSD as hidden layers.
4. All fonts used must be Google fonts.
5. You will need to supply the chosen home page plus one example page (example page as a style guide for how all other pages will look). Example page is only the header and navigational bar at the top, an empty sector in the middle with a column (190 px wide) which can be left or right aligned which means the main sector is 910 pixels wide, and then the footer at the bottom of the page

Checklist - http://layoutreviewlist.example/

Examples of some websites that have great design... don't copy them please but they are similar in look to what we are after....
http://www.pawnriverhub.example/

Industry/Entity Type

Printing

Font styles to use
Serif
Sans Serif

Requirements
Should not have
• Drop shadows, comic sans font

```html
<!DOCTYPE html>
<html lang="en">
<head>
<meta charset="utf-8">
<title>Inkvale – Printing &amp; Photocopying</title>
<link rel="stylesheet" href="https://fonts.googleapis.com/css2?family=Lato:wght@300;400;700&display=swap">
<style>
:root{
  --brand:#35399a;
  --brand-deep:#2c2f8c;
  --ink:#333338;
  --muted:#6b6b72;
  --tile:#f3f3f8;
  --band:#efefef;
  --field:#ffffff;
  --line:#dcdce2;
  --social:#c9c9cc;
}
*{box-sizing:border-box;margin:0;padding:0}
html,body{width:1200px;height:1088px;overflow:hidden;background:#fff}
body{position:relative;font-family:'Lato',Arial,sans-serif;color:var(--ink)}
a{color:inherit;text-decoration:none}

/* header */
.brand{position:absolute;left:271px;top:14px;display:flex;align-items:center;gap:8px}
.brand-dot{width:46px;height:46px;border-radius:50%;background:var(--brand)}
.brand-name{font-size:28px;font-weight:700;color:var(--brand)}
.top-links{position:absolute;right:271px;top:16px;display:flex;font-size:10px;color:var(--ink)}
.top-links a{padding:0 8px;border-left:1px solid #bbb;line-height:12px}
.top-links a:first-child{border-left:none}
.top-links a:last-child{padding-right:0}
.motto{position:absolute;left:271px;top:70px;width:315px}
.motto-quote{text-align:center;color:var(--brand);font-size:12px;font-weight:700}
.motto-sub{margin-top:4px;font-size:9.5px;font-weight:700;color:#4a4a50}
.contact{position:absolute;left:745px;top:70px;font-size:9.5px;color:#555}
.contact div{display:flex;align-items:center;gap:6px;height:16px}
.contact .phone{font-weight:700;color:var(--ink)}

/* main nav */
.main-nav{position:absolute;left:0;top:108px;width:1200px;height:30px;background:var(--brand);border-bottom:2px dotted #20235f}
.main-nav ul{list-style:none;display:flex;position:absolute;left:271px;top:8px;font-size:11px;color:#fff}
.main-nav li{margin-right:15px}

/* hero */
.hero{position:absolute;left:0;top:138px;width:1200px;height:239px;background:#000}
.hero-visual{position:absolute;left:234px;top:0;width:732px;height:239px;
  background:radial-gradient(ellipse at 70% 45%,#3b63c9 0%,#1b3a9a 35%,#0a1650 65%,#000 100%)}
.hero-title{position:absolute;left:270px;top:104px;color:#fff;font-size:24px;line-height:32px}
.hero-title .light{font-weight:300;display:block}
.hero-title .strong{font-weight:700;display:block}

/* services */
.services{position:absolute;left:288px;top:413px;display:grid;grid-template-columns:repeat(3,192px);grid-template-rows:repeat(2,102px);column-gap:24px;row-gap:24px}
.service{background:var(--tile);display:flex;flex-direction:column;align-items:center;justify-content:flex-end;padding-bottom:14px}
.service svg{margin-bottom:12px}
.service-label{font-size:14px;color:var(--ink)}
.service.is-open{align-items:flex-start;justify-content:flex-start;padding:10px 10px 8px 12px}
.service.is-open .service-label{font-size:14px;margin-bottom:4px}
.service.is-open p{font-size:8.6px;line-height:13px;color:#555}

/* quote */
.quote{position:absolute;left:0;top:677px;width:1200px;height:254px;background:var(--band)}
.quote-intro{position:absolute;left:271px;top:32px;width:205px}
.quote-intro h2{font-size:26px;line-height:32px;font-weight:300;color:var(--ink)}
.quote-intro h2 strong{display:block;font-weight:700;color:var(--brand)}
.quote-intro p{margin-top:12px;font-size:11px;line-height:15.5px;color:var(--ink)}
.field{position:absolute;background:var(--field);border:1px solid var(--line);border-radius:3px;font-size:9px;color:#888;padding:7px 8px}
.quote-btn{position:absolute;left:614px;top:193px;width:206px;height:25px;background:var(--brand);border:1px solid var(--brand-deep);border-radius:3px;color:#fff;font-weight:700;font-size:11px;display:flex;align-items:center;justify-content:center}

/* footer */
.footer-links{position:absolute;left:0;width:1200px;display:flex;justify-content:center;font-size:9.5px;color:var(--ink)}
.footer-links a{padding:0 9px;border-left:1px solid #bbb;line-height:11px}
.footer-links a:first-child{border-left:none}
.social{position:absolute;top:1020px;left:0;width:1200px;display:flex;justify-content:center;gap:10px}
.social span{width:22px;height:22px;border-radius:50%;background:var(--social)}
.copyright{position:absolute;top:1058px;width:1200px;text-align:center;font-size:9px;color:#555}
</style>
</head>
<body>

<header>
  <div class="brand"><span class="brand-dot"></span><span class="brand-name">Inkvale</span></div>
  <nav class="top-links">
    <a href="#">Home</a><a href="#">About</a><a href="#">Photocopying</a><a href="#">Printing</a><a href="#">Free Quote</a><a href="#">Contact</a>
  </nav>
  <div class="motto">
    <div class="motto-quote">“Sharp prints, every time”</div>
    <div class="motto-sub">Professional photocopying - digital &amp; film processing, design and printing</div>
  </div>
  <div class="contact">
    <div class="phone"><svg width="8" height="9" viewBox="0 0 8 9"><path d="M1.5 0.5l1.5 0 .7 2-1 .8c.5 1.2 1.2 2 2.3 2.5l.8-1 2 .7v1.5c0 .6-.5 1-1 1C3.3 8 0.5 5.3.5 1.5c0-.6.4-1 1-1z" fill="#999"/></svg>07. 555.0198</div>
    <div><svg width="8" height="10" viewBox="0 0 8 10"><path d="M4 0C1.8 0 0 1.7 0 3.8 0 6.5 4 10 4 10s4-3.5 4-6.2C8 1.7 6.2 0 4 0zm0 5.3a1.5 1.5 0 110-3 1.5 1.5 0 010 3z" fill="#999"/></svg>12/88 Harbour Lane - Kowhai - Marlow Bay</div>
  </div>
</header>

<nav class="main-nav">
  <ul>
    <li>Laminating</li><li>Business Cards</li><li>Typing Services</li><li>Film Processing</li><li>Photo Printing</li><li>Passport Photos</li><li>Image Restoration</li><li>Printer supplies</li>
  </ul>
</nav>

<section class="hero">
  <div class="hero-visual" role="img" aria-label="Close-up photograph of a blue-lit photocopier control panel"></div>
  <h1 class="hero-title"><span class="light">Digital Printing, Laminating And</span><span class="strong">Photocopying Services Throughout Marlow Bay</span></h1>
</section>

<section class="services">
  <div class="service is-open">
    <div class="service-label">Photocopying</div>
    <p>Cost effective photocopying<br>No matter the quantity of photocopies you need or the size of your copy - you can rely on us to provide a top quality service!</p>
  </div>
  <div class="service">
    <svg width="40" height="40" viewBox="0 0 40 40"><rect x="8" y="2" width="26" height="36" rx="2" fill="#2e3192"/><g fill="#fff"><rect x="5" y="7" width="6" height="2" rx="1"/><rect x="5" y="13" width="6" height="2" rx="1"/><rect x="5" y="19" width="6" height="2" rx="1"/><rect x="5" y="25" width="6" height="2" rx="1"/><rect x="5" y="31" width="6" height="2" rx="1"/></g><rect x="14" y="5" width="17" height="30" fill="none" stroke="#fff" stroke-width="1"/></svg>
    <div class="service-label">Laminating &amp; Binding</div>
  </div>
  <div class="service">
    <svg width="40" height="40" viewBox="0 0 40 40"><rect x="10" y="3" width="20" height="10" fill="#2e3192"/><rect x="2" y="14" width="36" height="16" rx="2" fill="#2e3192"/><rect x="9" y="24" width="22" height="14" fill="#fff" stroke="#2e3192" stroke-width="2"/><rect x="12" y="28" width="16" height="2" fill="#2e3192"/><rect x="12" y="32" width="16" height="2" fill="#2e3192"/></svg>
    <div class="service-label">Digital Printing</div>
  </div>
  <div class="service">
    <svg width="40" height="40" viewBox="0 0 40 40"><rect x="5" y="2" width="30" height="36" rx="2" fill="#2e3192"/><g fill="#fff"><rect x="7" y="5" width="3" height="3"/><rect x="7" y="11" width="3" height="3"/><rect x="7" y="17" width="3" height="3"/><rect x="7" y="23" width="3" height="3"/><rect x="7" y="29" width="3" height="3"/><rect x="30" y="5" width="3" height="3"/><rect x="30" y="11" width="3" height="3"/><rect x="30" y="17" width="3" height="3"/><rect x="30" y="23" width="3" height="3"/><rect x="30" y="29" width="3" height="3"/><rect x="13" y="5" width="14" height="13"/><rect x="13" y="21" width="14" height="13"/></g></svg>
    <div class="service-label">Film Processing</div>
  </div>
  <div class="service">
    <svg width="44" height="40" viewBox="0 0 44 40"><rect x="18" y="1" width="8" height="8" rx="1" fill="none" stroke="#2e3192" stroke-width="2"/><rect x="2" y="6" width="40" height="32" rx="3" fill="none" stroke="#2e3192" stroke-width="3"/><rect x="7" y="15" width="12" height="16" fill="#2e3192"/><g fill="#2e3192"><rect x="23" y="16" width="14" height="2"/><rect x="23" y="21" width="14" height="2"/><rect x="23" y="26" width="10" height="2"/></g></svg>
    <div class="service-label">Business Cards</div>
  </div>
  <div class="service">
    <svg width="40" height="40" viewBox="0 0 40 40"><rect x="12" y="2" width="16" height="14" fill="#fff" stroke="#2e3192" stroke-width="2"/><path d="M14 14l5-6 4 4 3-3 1 5z" fill="#2e3192"/><rect x="2" y="16" width="36" height="16" rx="2" fill="#2e3192"/><rect x="9" y="28" width="22" height="10" fill="#fff" stroke="#2e3192" stroke-width="2"/></svg>
    <div class="service-label">Photo Printing</div>
  </div>
</section>

<section class="quote">
  <div class="quote-intro">
    <h2>Get<strong>A Free Quote</strong></h2>
    <p>Talk to our team about your requirements. Please fill out the form below and we will contact you within a day.</p>
    <p>You can now upload and send us your file for a free quote!</p>
  </div>
  <div class="field" style="left:505px;top:38px;width:206px;height:25px">First Name</div>
  <div class="field" style="left:724px;top:38px;width:206px;height:25px">Last Name</div>
  <div class="field" style="left:505px;top:77px;width:206px;height:25px">Email Address</div>
  <div class="field" style="left:724px;top:77px;width:206px;height:25px">Phone Number</div>
  <div class="field" style="left:505px;top:113px;width:425px;height:67px">Message</div>
  <div class="quote-btn">GET A QUOTE</div>
</section>

<footer>
  <nav class="footer-links" style="top:966px">
    <a href="#">Home</a><a href="#">About</a><a href="#">Photocopying</a><a href="#">Printing</a><a href="#">Laminating</a><a href="#">Business Cards</a><a href="#">Typing Services</a><a href="#">Film Processing</a><a href="#">Photo Printing</a>
  </nav>
  <nav class="footer-links" style="top:985px">
    <a href="#">Passport Photos</a><a href="#">Image Restoration</a><a href="#">Printer Supplies</a><a href="#">Free Quote</a><a href="#">Contact</a>
  </nav>
  <div class="social" aria-label="Social links"><span></span><span></span><span></span><span></span></div>
  <div class="copyright">Copyright © 2015 Inkvale. All Rights Reserved.</div>
</footer>

</body>
</html>
```